Website for Scientific & Engineering Organization

Overview

The objective is to design a professional, easy-to-navigate, and visually appealing website for the <Enclosed Organization (see attached files)>, reflecting their esteemed status in the engineering and scientific community.

Pages:

Home (About Us) : Introduce the organization, highlighting their activities, history, and fellowship. Include a section for latest news highlights.

News and Programme : Dedicated page for news updates and detailed annual programmes

Gallery : This page will feature photographs and descriptions of the society's 'Voyages' and events.

Downloads : A section offering downloadable content such as newsletters and lecture materials, organized for user-friendliness.

Members Section : A private area for members to access exclusive content. Alternatively, a 'Membership' page with joining details and benefits if more public-facing content is preferred.

Design Elements:

Layout : A linear layout with a fixed top navigation bar for easy movement between pages.
Color Scheme : Utilize the provided colors (#395394, #E00053, #0043E1) to create a cohesive and professional aesthetic.
Typography : Use a combination of serif for headings and sans-serif for body text, ensuring readability and elegance.

Features:

Responsive Design : The design will accommodate various devices, ensuring consistency across mobiles, tablets, and desktops.

Accessibility : Design for all users with adequate spacing around elements and color contrasts

Content Strategy (Visual Focus):

Home Page : Visual emphasis on the introduction, mission, and recent 'Voyages' with engaging imagery and concise text.
News and Programme : Clear, visually distinct sections for news and the annual schedule
Gallery : A visually rich page with a grid or album layout, allowing users to easily browse through the years and events.
Downloads : Neatly organized sections with clear labels and icons to represent the different types of available downloads. Downloads are PDF newsletter/flyers/programmes etc...
Members Section/Membership : A design that conveys exclusivity and value, encouraging sign-ups and engagement from members.
Design Considerations:

Consistency : Ensure the design reflects the organization's heritage and professionalism throughout all pages.
User Experience : Focus on intuitive navigation and information architecture to guide visitors smoothly through the site.
Visual Hierarchy : Use size, color, and layout to emphasize key areas and direct user attention effectively.
Final Notes:

This design spec focuses on creating a web presence that mirrors the organization's prestige and heritage, providing an engaging, informative platform for members and the public alike. The design will be crafted to allow for easy content updates and adaptability, ensuring a long-lasting and effective website.

Target Market(s)

Non profit science and engineering. Older people

Industry/Entity Type

Non profit scientific organization

Number of Pages Required

5+ page

Requirements
Should not have
• No search feature

```html
<!DOCTYPE html>
<html lang="en">
<head>
<meta charset="utf-8">
<title>Orbis Society British Section</title>
<link href="https://fonts.googleapis.com/css2?family=Montserrat:wght@400;500;600;700&display=swap" rel="stylesheet">
<style>
:root{
  --blue:#395394;
  --red:#d8004c;
  --ink:#111111;
  --grey:#6b6f7a;
  --header:#e6eaf8;
  --white:#ffffff;
  --black:#000000;
}
*{margin:0;padding:0;box-sizing:border-box}
html,body{width:1200px;height:4023px;overflow:hidden}
body{position:relative;font-family:'Montserrat',sans-serif;color:var(--ink);background:var(--white)}
.abs{position:absolute}
a{color:inherit}

/* header */
.site-header{left:0;top:0;width:1200px;height:86px;background:var(--header);z-index:5}
.brand-box{left:89px;top:0;width:266px;height:137px;background:var(--white);border-radius:0 0 8px 8px;box-shadow:0 2px 8px rgba(0,0,0,.12);z-index:6;display:flex;flex-direction:column;align-items:center;justify-content:center;gap:4px}
.brand-row{display:flex;align-items:center;gap:10px}
.brand-dot{width:22px;height:22px;border-radius:50%;background:var(--blue)}
.brand-name{font-size:26px;font-weight:700;color:var(--blue)}
.brand-sub{font-size:13px;font-weight:700;color:var(--blue)}
.main-nav{left:381px;top:35px;display:flex;gap:24px;font-size:13px;font-weight:500;z-index:6}

/* hero */
.hero{left:0;top:86px;width:1200px;height:560px;background:linear-gradient(100deg,#3a3a3d 0%,#6d6a66 35%,#a59a8c 60%,#c9a43a 80%,#e4b315 100%)}
.hero-title{left:109px;top:224px;font-size:38px;font-weight:700;line-height:44px;color:var(--white)}
.hero-sub{left:110px;top:378px;font-size:17px;font-weight:600;color:var(--white)}
.btn{display:flex;align-items:center;justify-content:center;border-radius:24px;font-size:15px;font-weight:600;color:var(--white);text-decoration:none}
.btn-outline{left:112px;top:436px;width:196px;height:46px;border:3px solid var(--white)}
.btn-red{background:var(--red)}
.btn-blue{background:var(--blue)}

/* features */
.features{left:31px;top:608px;width:1130px;height:269px;background:var(--blue);border-radius:12px;display:flex}
.feature{flex:1;display:flex;flex-direction:column;align-items:center;color:var(--white);text-align:center;font-size:14.5px;line-height:29px;padding-top:24px}
.feature+.feature{border-left:1px solid rgba(255,255,255,.5);margin:30px 0 36px;padding-top:0}
.feature:first-child{margin:0}
.feature svg{margin-bottom:12px}
.feature p{width:360px}
.feature .wide{font-size:16px;margin-top:20px}
.btn-join{width:196px;height:46px;margin-top:22px}

/* who */
.who-title{left:0;top:940px;width:1200px;text-align:center;font-size:38px;font-weight:700}
.who-text{left:152px;top:1014px;width:896px;text-align:center;font-size:14px;line-height:26px;color:var(--grey)}

/* bands */
.band-svg{left:0;width:1200px}
.section-title{font-size:40px;font-weight:700}
.body-text{font-size:14px;line-height:26px}
.photo{border-radius:4px}
.frame{border-radius:6px;border:3px solid}

.act-frame{left:325px;top:1242px;width:231px;height:185px;border-color:var(--white)}
.act-photo{left:109px;top:1278px;width:411px;height:322px;background:linear-gradient(135deg,#d7a53a 0%,#3c4d66 35%,#1f2c45 70%,#56708e 100%)}
.act-title{left:600px;top:1228px;color:var(--white)}
.act-text{left:600px;top:1298px;width:452px;color:var(--white)}

.hist-title{left:109px;top:1806px}
.hist-text{left:110px;top:1872px;width:452px;color:var(--grey)}
.hist-photo{left:617px;top:1798px;width:411px;height:322px;background:linear-gradient(180deg,#8aa3c6 0%,#c9c2bd 45%,#a17a5c 75%,#7a6350 100%)}

.mem-photo{left:119px;top:2242px;width:412px;height:324px;background:linear-gradient(180deg,#9ea5ad 0%,#7d7d7f 45%,#6a4a55 80%,#3d3f55 100%)}
.mem-title{left:602px;top:2206px}
.mem-text{left:602px;top:2272px;width:452px;color:var(--grey)}

/* news */
.news-title{left:0;top:2720px;width:1200px;text-align:center;color:var(--white)}
.card{background:var(--white);border-radius:4px;top:2800px;height:388px;padding:4px}
.card-img{width:100%}
.card-body{padding:14px 12px 0;font-size:13px;line-height:27px}
.card-body h3{font-size:15px;font-weight:600;line-height:28px}
.date{display:flex;align-items:center;gap:6px;font-weight:600;font-size:12.5px}
.card-body a{font-weight:600;color:var(--blue)}
.card-lead .card-body h3{font-size:24px;line-height:31px;padding-top:4px}
.card-lead .date{font-size:15px;margin-top:8px}

.tagline{left:0;top:3446px;width:1200px;text-align:center;font-size:27px;font-weight:700;line-height:36px}

/* footer */
.footer-brand{left:0;top:3700px;width:1200px;display:flex;flex-direction:column;align-items:center;gap:6px}
.footer-brand .brand-name,.footer-brand .brand-sub{color:var(--white)}
.footer-brand .brand-dot{background:var(--white)}
.social{left:0;top:3840px;width:1200px;display:flex;justify-content:center;gap:40px}
.social span{width:38px;height:38px;border:2px solid var(--white);border-radius:50%;display:flex;align-items:center;justify-content:center}
.footer-nav{left:0;top:3906px;width:1200px;display:flex;justify-content:center;gap:24px;color:var(--white);font-size:13px;font-weight:500}
.footer-rule{left:109px;top:3964px;width:980px;height:1px;background:var(--white)}
.copyright{left:0;top:3981px;width:1200px;text-align:center;color:var(--white);font-size:13px}
</style>
</head>
<body>

<header class="abs site-header"></header>
<div class="abs brand-box">
  <div class="brand-row"><span class="brand-dot"></span><span class="brand-name">Orbis Society</span></div>
  <span class="brand-sub">British Section</span>
</div>
<nav class="abs main-nav">
  <span>ABOUT US</span><span>NEWS &amp; PROGRAMME</span><span>GALLERY</span><span>DOWNLOADS</span><span>CONTACT US</span><span>MEMBERS SECTION</span>
</nav>

<section class="abs hero" role="img" aria-label="Photo of two engineers shaking hands over a desk with a yellow hard hat in the foreground"></section>
<h1 class="abs hero-title">Welcome To<br>The British Section of<br>The Orbis Society</h1>
<p class="abs hero-sub">Sharing Knowledge and a Love of France</p>
<a class="abs btn btn-outline">Get Started</a>

<section class="abs features">
  <div class="feature">
    <svg width="80" height="80" viewBox="0 0 80 80" fill="#fff"><path d="M12 46a28 28 0 0 1 56 0z"/><rect x="34" y="8" width="12" height="20" rx="3"/><rect x="8" y="48" width="64" height="8" rx="3"/><circle cx="40" cy="66" r="10" fill="none" stroke="#fff" stroke-width="5"/></svg>
    <p>An informal society of engineers and scientists, giving equal importance to the quality of our technical activities and our fellowship.</p>
  </div>
  <div class="feature">
    <svg width="100" height="80" viewBox="0 0 100 80" fill="none" stroke="#fff" stroke-width="5"><circle cx="50" cy="40" r="22"/><path d="M50 26l10 14-10 14-10-14z"/><path d="M12 6v68M6 6v18h12V6M88 6c-6 6-6 22 0 26v42"/></svg>
    <p>We provide high quality lectures and technical visits on diverse engineering and scientific subjects, and the enjoyment of French culture and Cuisine.</p>
  </div>
  <div class="feature">
    <svg width="80" height="86" viewBox="0 0 80 86" fill="#fff"><circle cx="34" cy="20" r="16"/><path d="M6 76c0-22 12-34 28-34s22 8 24 14H40v20z"/><circle cx="58" cy="66" r="16"/><path d="M58 58v16M50 66h16" stroke="#395394" stroke-width="4"/></svg>
    <p class="wide">New members are always welcome</p>
    <a class="btn btn-red btn-join">Learn More</a>
  </div>
</section>

<h2 class="abs who-title">Who We Are</h2>
<p class="abs who-text">We are an informal society of engineers and scientists. A very friendly organisation where equal importance is given to the quality of our technical activities and our fellowship, where our partners are involved and welcomed in everything we do. For more information please click the link to our <a>Brochure</a></p>

<svg class="abs band-svg" style="top:1136px" height="548" viewBox="0 0 1200 548" preserveAspectRatio="none"><polygon points="0,6 176,34 1200,10 1200,548 0,548" fill="#d8004c"/><polygon points="0,16 176,44 1200,20 1200,548 0,548" fill="#395394"/></svg>
<div class="abs frame act-frame"></div>
<div class="abs photo act-photo" role="img" aria-label="Photo of an engineer in a hard hat working at a computer showing a gear design"></div>
<h2 class="abs section-title act-title">Our Activities</h2>
<p class="abs body-text act-text">Five or six high quality technical lectures are arranged throughout the year at a number of London venues followed by dinner. Memorable lectures have included topics as diverse as the building of the Panama Canal, the origins of SI standard measurements and the current Antarctic research programme. There are normally two ‘Voyages’ each year of three or four days each, generally but not exclusively to France, where visits to technical or cultural establishments and major construction sites are untaken.</p>
<a class="abs btn btn-red" style="left:600px;top:1553px;width:196px;height:45px">Learn More</a>

<h2 class="abs section-title hist-title">Our History</h2>
<p class="abs body-text hist-text">The British Section of the National Council of Technical Sciences of France was founded on 27th June 1919 by members of the British Army returning from the war who wished to maintain links with their wartime colleagues in France. For more information click History or browse online L’Entente Cordiale - 100years of the British Section of the Orbis Society <a style="color:var(--blue);font-weight:600">click Link.</a></p>
<a class="abs btn btn-blue" style="left:108px;top:2055px;width:196px;height:47px">Learn More</a>
<div class="abs frame" style="left:833px;top:1762px;width:231px;height:186px;border-color:var(--blue)"></div>
<div class="abs photo hist-photo" role="img" aria-label="Photo of a historic stone aqueduct arch above a town"></div>

<div class="abs frame" style="left:336px;top:2206px;width:230px;height:186px;border-color:var(--red)"></div>
<div class="abs photo mem-photo" role="img" aria-label="Group photo of society members on a voyage in front of a bridge"></div>
<h2 class="abs section-title mem-title">Our Members</h2>
<p class="abs body-text mem-text">The origins of the Section lie in civil engineering. For many years, however, in line with the now named Orbis Society of French Engineers, we have been open to membership from like minded people from all fields of engineering and science. We are always delighted to welcome new members. If you would like to join us or would like further information on membership, please click Membership, contact an existing member, or the Membership Secretary, Alan Marsh, <a style="color:var(--blue);font-weight:600">membership@orbis-uk.example</a></p>
<a class="abs btn btn-blue" style="left:598px;top:2527px;width:197px;height:45px">Learn More</a>

<svg class="abs band-svg" style="top:2636px" height="726" viewBox="0 0 1200 726" preserveAspectRatio="none"><polygon points="0,6 176,34 1200,10 1200,726 0,726" fill="#d8004c"/><polygon points="0,16 176,44 1200,20 1200,726 0,726" fill="#395394"/></svg>
<h2 class="abs section-title news-title">Recent News</h2>

<article class="abs card card-lead" style="left:102px;width:478px">
  <div class="card-img" style="height:250px;background:linear-gradient(135deg,#cfcfcf,#6e6e6e 55%,#2f2f2f)" role="img" aria-label="Photo of a burnt chair after a fire test"></div>
  <div class="card-body">
    <h3>Incoming President’s Inaugural lecture and dinner</h3>
    <div class="date"><svg width="22" height="22" viewBox="0 0 22 22" fill="none" stroke="#111" stroke-width="2"><rect x="2" y="4" width="18" height="16" rx="2"/><path d="M2 9h18M7 1v5M15 1v5"/></svg>Jan 29,2024</div>
  </div>
</article>
<article class="abs card" style="left:594px;width:244px">
  <div class="card-img" style="height:187px;background:linear-gradient(180deg,#3a1a0c,#c94a10 55%,#f7b12c)" role="img" aria-label="Photo of a forest fire at night"></div>
  <div class="card-body">
    <h3>Evening Lecture and Dinner</h3>
    <div class="date"><svg width="17" height="17" viewBox="0 0 22 22" fill="none" stroke="#111" stroke-width="2"><rect x="2" y="4" width="18" height="16" rx="2"/><path d="M2 9h18M7 1v5M15 1v5"/></svg>Mar 19,2024</div>
    <div>by Professor Daniel Ferris</div>
    <div>At Harcourt Hall</div>
    <a>Read More...</a>
  </div>
</article>
<article class="abs card" style="left:850px;width:244px">
  <div class="card-img" style="height:187px;background:linear-gradient(180deg,#7f9ab8,#a0a6ad 50%,#5f5a4d)" role="img" aria-label="Photo of smoke rising from a burning tower block"></div>
  <div class="card-body">
    <h3>Evening Lecture and Dinner</h3>
    <div class="date"><svg width="17" height="17" viewBox="0 0 22 22" fill="none" stroke="#111" stroke-width="2"><rect x="2" y="4" width="18" height="16" rx="2"/><path d="M2 9h18M7 1v5M15 1v5"/></svg>Apr 30,2024</div>
    <div>by Mark Ellison</div>
    <div>At Linden House</div>
    <a>Read More...</a>
  </div>
</article>
<a class="abs btn btn-red" style="left:502px;top:3241px;width:196px;height:47px">View More</a>

<p class="abs tagline">The Society for Engineers and Scientists where they sample<br>French cuisine and culture with their partners as well as<br>continue their professional interests</p>

<svg class="abs band-svg" style="top:3572px" height="451" viewBox="0 0 1200 451" preserveAspectRatio="none"><polygon points="0,6 176,34 1200,10 1200,451 0,451" fill="#d8004c"/><polygon points="0,16 176,44 1200,20 1200,451 0,451" fill="#000"/></svg>
<div class="abs footer-brand">
  <div class="brand-row"><span class="brand-dot"></span><span class="brand-name">Orbis Society</span></div>
  <span class="brand-sub">British Section</span>
</div>
<div class="abs social">
  <span><svg width="18" height="18" viewBox="0 0 24 24" fill="none" stroke="#fff" stroke-width="2"><path d="M5 3h4l2 5-3 2a12 12 0 0 0 6 6l2-3 5 2v4a2 2 0 0 1-2 2A18 18 0 0 1 3 5a2 2 0 0 1 2-2z"/></svg></span>
  <span><svg width="18" height="18" viewBox="0 0 24 24" fill="none" stroke="#fff" stroke-width="2"><rect x="3" y="5" width="18" height="14" rx="2"/><path d="M3 7l9 6 9-6"/></svg></span>
  <span><svg width="18" height="18" viewBox="0 0 24 24" fill="none" stroke="#fff" stroke-width="2"><path d="M12 4v16M8 12h8"/></svg></span>
</div>
<nav class="abs footer-nav"><span>ABOUT US</span><span>NEWS &amp; PROGRAMME</span><span>GALLERY</span><span>DOWNLOADS</span><span>CONTACT US</span><span>MEMBERS SECTION</span></nav>
<div class="abs footer-rule"></div>
<p class="abs copyright">Copyright © 2024 Orbis Society | All Rights Reserved</p>

</body>
</html>
```